Premium modern eliquids labels 84.5 x 80 mm

I am looking for modern graphics for the labels of a new eliquid line that will have 4 different types of eliquids. It will have a tobacco one (brown colours maybe), a fruity one (bright colours maybe), a minty one (green colours maybe) and a creamy one (beige colours maybe).
I will need one of them to see how the design is, that design will have to be adapted to the other 3 colours of the label.
The brand logo is attached. I also attached a sample of what is mandatory to write on the label, you can change size, place and font of what is written, the only thing that cannot be reduced is the yellow parts. I attach the bottle that we will use.The size of the label is 84.5 x 80 mm (base x height).

Target Market(s)

vapers

Requirements
Must have
• My project must have one of the labels.

```html
<!DOCTYPE html>
<html lang="en">
<head>
<meta charset="utf-8">
<title>Northdrift Tobacco E-Liquid Label</title>
<link href="https://fonts.googleapis.com/css2?family=Russo+One&family=Oswald:wght@600&display=swap" rel="stylesheet">
<style>
  :root {
    --page: #ffffff;
    --tobacco: #c4663a;
    --tobacco-deep: #b85a30;
    --frame-gold: #f4a93c;
    --ink: #2f2925;
    --splash: #b9b9bb;
    --brand-blue: #5fb2e2;
    --white: #ffffff;
  }
  html, body {
    margin: 0;
    width: 1200px;
    height: 1200px;
    overflow: hidden;
    background: var(--page);
  }
  .label {
    position: absolute;
    left: 370px;
    top: 80px;
    width: 460px;
    height: 1040px;
    background: var(--tobacco);
    overflow: hidden;
  }
  .brand {
    position: absolute;
    left: 0;
    top: 110px;
    width: 100%;
    display: flex;
    justify-content: center;
    align-items: center;
    gap: 14px;
  }
  .brand-dot {
    width: 26px;
    height: 26px;
    border-radius: 50%;
    background: var(--brand-blue);
  }
  .brand-name {
    font-family: "Russo One", sans-serif;
    font-size: 50px;
    color: var(--brand-blue);
    letter-spacing: 1px;
  }
  .splash {
    position: absolute;
    left: 0;
    top: 468px;
    width: 460px;
    height: 423px;
    background: var(--splash);
    border-radius: 46% 54% 40% 60% / 50% 40% 60% 50%;
  }
  .flavour-box {
    position: absolute;
    left: -159px;
    top: 470px;
    width: 648px;
    height: 212px;
    transform: rotate(-90deg);
    box-sizing: border-box;
    border: 8px solid var(--frame-gold);
    outline: 4px solid var(--ink);
    border-radius: 34px;
    background: var(--tobacco-deep);
    display: flex;
    align-items: center;
    justify-content: center;
  }
  .flavour-name {
    font-family: "Russo One", sans-serif;
    font-size: 124px;
    color: var(--white);
    -webkit-text-stroke: 5px var(--ink);
    paint-order: stroke fill;
    letter-spacing: 2px;
    line-height: 1;
  }
  .product-type {
    position: absolute;
    left: 198px;
    top: 695px;
    width: 288px;
    height: 105px;
    transform: rotate(-90deg);
    display: flex;
    align-items: center;
    justify-content: center;
    font-family: "Russo One", sans-serif;
    font-size: 62px;
    color: var(--white);
    -webkit-text-stroke: 4px var(--ink);
    paint-order: stroke fill;
    line-height: 1;
  }
  .volume {
    position: absolute;
    left: 0;
    top: 920px;
    width: 100%;
    text-align: center;
    font-family: "Oswald", sans-serif;
    font-weight: 600;
    font-size: 36px;
    color: var(--white);
  }
  .base-band {
    position: absolute;
    left: 0;
    width: 100%;
    background: var(--white);
  }
  .base-band.upper { top: 990px; height: 6px; }
  .base-band.lower { top: 1006px; height: 6px; }
</style>
</head>
<body>
  <main class="label">
    <div class="brand">
      <span class="brand-dot"></span>
      <span class="brand-name">NORTHDRIFT</span>
    </div>
    <div class="splash" role="img" aria-label="Grey liquid splash illustration"></div>
    <div class="flavour-box"><span class="flavour-name">TOBACCO</span></div>
    <div class="product-type">E-LIQUID</div>
    <div class="volume">20 ml E-LIQUID</div>
    <div class="base-band upper"></div>
    <div class="base-band lower"></div>
  </main>
</body>
</html>
```